Design Project for Digital Recruitment Business

I am launching a new website in the Digital Marketing Recruitment space here in the UK.We are a start up so this very much phase 1 with our web offering.

Key points:

- I think it will be aproximately 5- 8 pages

- I am looking for wordpress(open on this)) design and coding/ development.

- It really is going to be a brochure site on the whole so don't expect any huge integration. I would like an RSS feed to publish our jobs on our site. I can get the code for that from my recruitment database partner Quillpost, all i will need is a blank page for that section?.Parley net,chirrup etc as well.

-I already have the logo.(See attached)which you guys delivered brilliantly on :-)

some reference sites I like the look of: http://www.orbitvale.example.co.uk http://www.ratchethouse.example.com/ http://www.webmavens.example.co.uk/

The menu bar on these sites are good, the language is good.I want contemporary and professional.It needs to connect to the viewer.
WE are in the social media space so that needs to fit/blend eg parleynet,GS.

SUGGESTED APPROACH
So I guess the best starting point would be to just submit a home page design so i can judge the styles I like best.Then the finalists of that round can submit another section of the website to see the consistency in terms of look and feel. I will then pick someone to work one on one with to complete the design and do the coding. That way no one gets to waste valuable time and energy :-)

Feel free to ping me questions
Updates

Reason: Hello All, I am going to extend by a few days. I have been inundated with work.However I Plan to look at all your designs this week end and respond to all your Queries. Thanks for your Patience.

Hi guys

here is a little more about us

We know that the career success of the candidates we place can have a great impact on the success of your business. We have built a network of talented industry professionals and an extensive knowledge of the market and its changing trends. We focus on career management,advice and consultancy.With over 30 years experience in our team we feel confident we can deliver. Our specialisms are Creative and Design,Digital Marketing,Editorial and Content,User Experience,and Technology related to building Websites.

In today's world of continually adapting,surviving and thriving we recognise that you rise and fall by the people you hire.That is why an expert  is required to help find those people in business critical roles. So if your online Marketing strategy is behind the times or your website traffic is poor for example we can help find people on a contract and permanent basis to bridge the gap in you marketing and E-commerce team. Pixel Scouts are specialists in these areas and offer a consultative approach to working with your business. If your business grows as a result of the people you recruited through us we could not be happier. Honest,straightforward,professional.

In terms of home page the Menu bar is 4-5 topics at most. 90% of the traffic to this website will be Candidates so Jobs will be the best content along with the 6 skill sets/categories and everything social after that.Very like Ratchet website I mentioned in the Brief. A couple of you are on the right tracks.
Hope this helps for now. I feel confident I can pick from one of you.

Kind regards

Martin

Soory one other thing,

RE; Images

People are tricky to do on Recruitment websites as its very PC and they dont look real enough.Animations of people are better in my humble opinion...

open to ideas/options

Thanks

Target Market(s)

marketeers,designers,ecommerce folks.

Industry/Entity Type

Business

Requirements
Must have
• open at this stage but obviously the logo design colours must sync with the overall look and feel.GS,chirrup,mingle+ must be dominant

```html
<!DOCTYPE html>
<html lang="en">
<head>
<meta charset="utf-8">
<title>Pixel Scouts — Digital Recruitment</title>
<link href="https://fonts.googleapis.com/css2?family=Questrial&display=swap" rel="stylesheet">
<style>
:root{
  --orange:#ff6a00;
  --orange-deep:#f04a0c;
  --purple:#3d1a8a;
  --navy:#1d1a6b;
  --grey-text:#6b6b6b;
  --grey-light:#c9c9c9;
  --green:#2f7d12;
  --plum:#4b0f3a;
  --gold:#8a6a00;
  --footer:#0d0d0d;
  --font:"Questrial",sans-serif;
}
*{box-sizing:border-box;margin:0;padding:0}
html,body{width:1066px;height:1200px;overflow:hidden;background:#fff;font-family:var(--font)}
.page{position:relative;width:1066px;height:1200px}
.abs{position:absolute}

.topbar{left:0;top:0;width:1066px;height:42px;background:linear-gradient(90deg,var(--orange-deep),#ff8a2a 40%,var(--orange) 70%,var(--orange-deep));border-bottom:1px solid #b34a9a}
.main-nav{left:397px;top:12px;display:flex;gap:0;color:#fff;font-size:13px}
.main-nav a{color:#fff;text-decoration:none;margin-right:37px}
.main-nav .active{position:relative}
.main-nav .active::after{content:"";position:absolute;left:50%;top:24px;margin-left:-6px;border:6px solid transparent;border-bottom-color:var(--purple);border-top:0}

.logo-box{left:89px;top:0;width:258px;height:86px;background:#fff;border:1px solid var(--orange);border-top:0;border-radius:0 0 4px 4px;box-shadow:0 1px 3px rgba(0,0,0,.2);display:flex;align-items:center;justify-content:center;gap:8px}
.brand-dot{width:30px;height:30px;border-radius:50%;background:var(--orange)}
.brand-name{font-size:28px;color:var(--purple);letter-spacing:-.5px}

.social{left:811px;top:89px;display:flex;gap:10px}
.social span{width:23px;height:23px;border-radius:50%;border:2px solid var(--grey-light)}

.cat-bar{left:89px;top:122px;width:888px;height:30px;background:linear-gradient(#f2f2f2,#d8d8d8);box-shadow:0 1px 2px rgba(0,0,0,.15)}
.cat-bar a{position:absolute;top:6px;color:var(--purple);text-decoration:none;font-size:16px}
.cat-bar a.small{font-size:13px;top:9px}
.cat-bar .sep{position:absolute;top:6px;width:1px;height:24px;background:#b9b9b9}
.search{position:absolute;left:676px;top:3px;width:208px;height:22px;background:#fff;border-radius:2px;font-size:10px;color:#555;padding:5px 6px}
.search svg{position:absolute;right:8px;top:4px}

.hero{left:89px;top:152px;width:888px;height:379px;background:linear-gradient(90deg,#a9a9a9,#d6d6d6 40%,#bdbdbd 70%,#e5e5e5)}

.features{left:89px;top:531px;width:888px;height:89px;background:repeating-linear-gradient(90deg,#c4c4c4 0 2px,#d4d4d4 2px 4px),linear-gradient(#ccc,#aaa);box-shadow:0 2px 3px rgba(0,0,0,.25)}
.feature{position:absolute;top:0;height:89px;display:flex;align-items:center;gap:10px}
.feature .icon{width:40px;height:40px;border-radius:50%;border:2px solid #888;display:flex;align-items:center;justify-content:center}
.feature .t1{font-size:21px;line-height:1}
.feature .t2{font-size:12px;line-height:1.1}
.feature .divider{position:absolute}
.fsep{position:absolute;top:0;width:1px;height:89px;background:#999;box-shadow:1px 0 0 #e0e0e0}

.jobs{left:85px;top:626px;width:436px;height:346px;box-shadow:1px 0 3px rgba(0,0,0,.12)}
.section-title{position:absolute;font-size:16px;color:#333}
.dash{position:absolute;border-top:1px dashed #777}
.job{position:absolute;left:7px;width:401px;height:46px;border-bottom:1px solid #eee}
.job .day{position:absolute;left:3px;top:2px;font-size:17px;color:#999}
.job .mon{position:absolute;left:3px;top:22px;font-size:12px;color:#444}
.job .role{position:absolute;left:46px;top:2px;font-size:14px;color:#777}
.job .place{position:absolute;left:46px;top:20px;font-size:15px;color:var(--navy)}
.view-all{position:absolute;left:364px;top:330px;font-size:11px;color:var(--orange);text-decoration:underline}

.about{left:538px;top:626px;width:430px}
.about p{position:absolute;left:2px;width:422px;font-size:11.5px;line-height:16px;color:var(--grey-text)}
.about .more{color:#777;text-decoration:underline}

.footer{left:0;top:972px;width:1066px;height:228px;background:var(--footer);border-top:4px solid var(--orange)}
.fcol{position:absolute;top:35px}
.fcol h4{font-weight:normal;color:#fff;font-size:14px;margin-bottom:23px}
.fcol a{display:block;width:max-content;padding-right:8px;color:#666;font-size:11px;text-decoration:none;height:26.6px;line-height:16px;border-bottom:1px solid #222;margin-bottom:0;padding-top:4px}
.ftab{left:741px;top:1px;width:241px;height:42px}
.flogo{position:absolute;left:38px;top:8px;display:flex;align-items:center;gap:6px}
.flogo .brand-dot{width:22px;height:22px}
.flogo .brand-name{font-size:20px}
.contact{position:absolute;left:743px;top:71px;width:240px;text-align:center;color:#fff;font-size:11px;line-height:13px}
.contact .gap{height:13px}
.contact .rule{border-top:1px solid #333;margin:6px 20px 7px}
.contact .legal{color:var(--orange);line-height:17px}
</style>
</head>
<body>
<div class="page">

  <header>
    <div class="abs topbar"></div>
    <nav class="abs main-nav">
      <a class="active">home</a><a>clients</a><a>candidates</a><a>jobs</a><a>about us</a><a>resources</a><a>contact us</a>
    </nav>
    <div class="abs logo-box"><span class="brand-dot"></span><span class="brand-name">pixelscouts</span></div>
    <div class="abs social" aria-label="Social links"><span></span><span></span><span></span><span></span><span></span></div>
  </header>

  <div class="abs cat-bar">
    <a class="small" style="left:29px">browse our jobs</a>
    <span class="sep" style="left:141px"></span>
    <a style="left:160px">Media</a>
    <span class="sep" style="left:223px"></span>
    <a style="left:239px">Creative</a>
    <span class="sep" style="left:317px"></span>
    <a style="left:337px">Marketing</a>
    <span class="sep" style="left:423px"></span>
    <a style="left:438px">Content</a>
    <div class="search">Search
      <svg width="14" height="14" viewBox="0 0 14 14"><circle cx="5.5" cy="5.5" r="4" fill="none" stroke="#333" stroke-width="1.8"/><line x1="8.5" y1="8.5" x2="13" y2="13" stroke="#333" stroke-width="2.2"/></svg>
    </div>
  </div>

  <div class="abs hero" role="img" aria-label="Greyscale photo of a smiling professional with a laptop in a busy office"></div>

  <div class="abs features">
    <div class="feature" style="left:38px">
      <span class="icon" style="background:var(--navy)"><svg width="20" height="20" viewBox="0 0 20 20"><circle cx="8" cy="8" r="5.5" fill="none" stroke="#fff" stroke-width="2"/><line x1="12" y1="12" x2="17" y2="17" stroke="#fff" stroke-width="2.5"/></svg></span>
      <div><div class="t1" style="color:var(--purple)">ADVANCE</div><div class="t2" style="color:var(--purple)">SEARCH</div></div>
    </div>
    <span class="fsep" style="left:226px"></span>
    <div class="feature" style="left:260px">
      <span class="icon" style="background:var(--green)"><svg width="18" height="18" viewBox="0 0 18 18"><rect x="3" y="3" width="12" height="12" fill="#fff"/></svg></span>
      <div><div class="t1" style="color:var(--green)">DREAM</div><div class="t2" style="color:var(--green)">JOBS</div></div>
    </div>
    <span class="fsep" style="left:439px"></span>
    <div class="feature" style="left:478px">
      <span class="icon" style="background:var(--plum)"><svg width="18" height="18" viewBox="0 0 18 18"><rect x="4" y="2" width="10" height="14" fill="#fff"/><line x1="6" y1="6" x2="12" y2="6" stroke="#888"/><line x1="6" y1="9" x2="12" y2="9" stroke="#888"/><line x1="6" y1="12" x2="12" y2="12" stroke="#888"/></svg></span>
      <div><div class="t1" style="color:var(--plum)">UPLOAD</div><div class="t2" style="color:var(--plum)">YOUR RESUME</div></div>
    </div>
    <span class="fsep" style="left:652px"></span>
    <div class="feature" style="left:696px">
      <span class="icon" style="background:#b8900a"><svg width="18" height="18" viewBox="0 0 18 18"><path d="M9 2v9M6 8l3 3 3-3" stroke="#fff" stroke-width="2" fill="none"/><rect x="5" y="13" width="8" height="3" fill="#fff"/></svg></span>
      <div><div class="t1" style="color:var(--gold)">JOIN US</div><div class="t2" style="color:var(--gold)">PIXEL SCOUTS</div></div>
    </div>
  </div>

  <section class="abs jobs">
    <h2 class="section-title" style="left:7px;top:13px;font-weight:normal">Latest Jobs</h2>
    <span class="dash" style="left:7px;top:36px;width:401px"></span>
    <div class="job" style="top:44px"><span class="day">21</span><span class="mon">Oct</span><span class="role">MND SECRETARY</span><span class="place">at ferris mesh works ltd. ( New York )</span></div>
    <div class="job" style="top:94px"><span class="day">21</span><span class="mon">Oct</span><span class="role">MND SECRETARY</span><span class="place">at ferris mesh works ltd. ( New York )</span></div>
    <div class="job" style="top:140px"><span class="day">21</span><span class="mon">Oct</span><span class="role">MND SECRETARY</span><span class="place">at ferris mesh works ltd. ( New York )</span></div>
    <div class="job" style="top:186px"><span class="day">21</span><span class="mon">Oct</span><span class="role">MND SECRETARY</span><span class="place">at ferris mesh works ltd. ( New York )</span></div>
    <div class="job" style="top:231px"><span class="day">21</span><span class="mon">Oct</span><span class="role">MND SECRETARY</span><span class="place">at ferris mesh works ltd. ( New York )</span></div>
    <div class="job" style="top:274px"><span class="day">21</span><span class="mon">Oct</span><span class="role">MND SECRETARY</span><span class="place">at ferris mesh works ltd. ( New York )</span></div>
    <a class="view-all">View All</a>
  </section>

  <section class="abs about">
    <h2 class="section-title" style="left:0;top:13px;font-weight:normal">Pixel Scouts</h2>
    <span class="dash" style="left:0;top:36px;width:403px"></span>
    <p style="top:42px">Things move fast. So we need to think faster. We're here to share our digital knowledge, relationships and join the dots between you and the people who will make your business a success.</p>
    <p style="top:106px">We think it's our job to be the experts. And it's important to us that everyone at Orbitvale is interested in the ever-changing digital world.</p>
    <p style="top:154px">We know people in every nook and cranny of the industry. And our real skill is bringing all of the communities of the digital world together to give you an all round service that consistently delivers the results that you want.<br><span class="more">Read More</span></p>
  </section>

  <footer class="abs footer">
    <div class="fcol" style="left:88px"><h4>JOB SEEKERS</h4><a>Register Now</a><a>Post Resumes</a><a>Search Jobs</a><a>Get Jobs by Email</a><a>Login</a></div>
    <div class="fcol" style="left:290px"><h4>EMPLOYERS</h4><a>Register Now</a><a>Post Jobs</a><a>Search Resumes</a><a>Get Resumes by Email</a><a>Login</a></div>
    <div class="fcol" style="left:498px"><h4>INFORMATION</h4><a>About Us</a><a>Terms &amp; Conditions</a><a>Privacy &amp; Policy</a><a>Careers With Us</a><a>Contact Us</a></div>
    <div class="abs ftab">
      <svg width="241" height="42" viewBox="0 0 241 42"><path d="M0 0H241L226 32Q222 42 210 42H26Q14 42 10 32Z" fill="#fff"/></svg>
      <div class="flogo"><span class="brand-dot"></span><span class="brand-name">pixelscouts</span></div>
    </div>
    <div class="contact">
      24 Larkmoor Row<br>London<br>N4 7QZ
      <div class="gap"></div>Tel: 020 7946 0321
      <div class="gap"></div>Email: hello@orbitvale.example.co.uk
      <div class="rule"></div>
      <div class="legal">All rights reserved<br>© 2010 PIXEL SCOUTS</div>
    </div>
  </footer>

</div>
</body>
</html>
```